Wordpress Website - for cutting edge Artificial Intelligence company

We need a wordpress web site for our company Varnolix.

Objective:
- To promote our software products to potential customers (e.g. large corporations)
- To promote our software products to potential partners (e.g. software makers who want to bundle our software inside their products)
- To promote our company to potential Investors (venture capital funds, angel investors, etc.)

Sample content and proposed structure can be found in the attached file.
Company logo is also attached.

The Quillet logo should only be used in the section relating to the Quillet Product (e.g. Quillet Text & Quillet Speech)

Target Market(s)

Core Target Market:
- Large corporations (e.g. Major Banks, Retailers & Pharmaceutical companies) who could buy our software

Industry/Entity Type

Software

Coding

Coded - Design and coding required

Font styles to use
Sans Serif

Colors
ffffff
ec1f27
000000
757575
dfdfdf
9bcb3c

Requirements
Must have
• Functionality:
• - Designed in Wordpress (using tools from wordpress.org, not hosted on wordpress.com)
• - Must have a user friendly CMS module for us to make updates easily
• - Must be designed to look great across different devices
• - Must be designed to look great in English and Chinese (as well as other future languages).

```html
<!DOCTYPE html>
<html lang="en">
<head>
<meta charset="utf-8">
<title>Varnolix</title>
<link rel="stylesheet" href="https://fonts.googleapis.com/css2?family=Roboto:wght@400;500;700&family=Oswald:wght@400;500&display=swap">
<style>
:root{
  --red:#ec1f27;
  --green:#9bcb3c;
  --black:#000000;
  --grey:#757575;
  --light:#dfdfdf;
  --white:#ffffff;
  --panel:#f2f2f2;
  --footer:#2b2b2b;
  --footer-line:#444;
}
*{margin:0;padding:0;box-sizing:border-box}
html,body{width:671px;height:1200px;overflow:hidden;background:var(--white)}
body{font-family:'Roboto',Arial,sans-serif;color:var(--black);position:relative}
.abs{position:absolute}

.top-line{left:0;top:0;width:671px;height:3px;background:var(--red)}
.site-header{left:0;top:3px;width:671px;height:61px;background:var(--white);box-shadow:0 2px 4px rgba(0,0,0,.12);z-index:2}
.brand{left:50px;top:14px;display:flex;align-items:center;gap:7px}
.brand-mark{width:12px;height:12px;background:var(--red)}
.brand-name{font-size:22px;font-weight:700;color:var(--red);letter-spacing:1px}
.lang{left:569px;top:0;width:53px;height:13px;background:var(--red);border-radius:0 0 3px 3px;color:var(--white);font-size:6.5px;display:flex;align-items:center;justify-content:center;gap:3px}
.main-nav{right:49px;top:31px;display:flex;gap:14px;font-size:8.4px;color:#222;letter-spacing:.2px}

.hero{left:0;top:64px;width:671px;height:292px;background:radial-gradient(ellipse at 55% 40%,#c9ced3 0%,#a4abb3 55%,#7f878f 100%)}
.hero-title{left:0;top:212px;width:671px;text-align:center;font-family:'Oswald',Arial,sans-serif;color:var(--white);text-shadow:0 1px 3px rgba(0,0,0,.4)}
.hero-title .line1{font-size:23px;line-height:28px}
.hero-title .line2{font-size:15.5px;line-height:22px}
.slider-arrows{left:586px;top:321px;display:flex;gap:4px}
.slider-arrows span{width:16px;height:16px;border-radius:50%;background:rgba(40,40,40,.75);display:flex;align-items:center;justify-content:center}

.cta{top:356px;height:40px;display:flex;align-items:center;justify-content:center;gap:6px;color:var(--white);font-size:12.5px}
.cta-demo{left:0;width:334px;background:var(--green)}
.cta-contact{left:334px;width:337px;background:var(--red)}

.section-title{left:0;width:671px;text-align:center;font-size:15.5px;font-weight:400}
.section-title em{font-style:normal;color:var(--green)}
.news-title{top:426px}
.news-card{width:183px;height:155px;overflow:hidden}
.news-card .photo{width:100%;height:100%}
.news-card .caption{position:absolute;left:0;bottom:0;width:100%;height:39px;background:rgba(0,0,0,.72);color:var(--white);font-size:7.8px;line-height:12.5px;padding:7px 30px 0 14px;white-space:nowrap}
.news-card .caption svg{position:absolute;right:14px;top:13px}

.stories{left:0;top:808px;width:671px;height:238px;background:var(--panel)}
.stories-title{top:844px}
.story{width:170px;text-align:center}
.avatar{width:70px;height:70px;border-radius:50%;border:3px solid var(--white);box-shadow:0 1px 4px rgba(0,0,0,.3);margin:0 auto;background:linear-gradient(160deg,#d8d8d8,#9a8e86)}
.story h3{font-size:7.5px;font-weight:500;margin-top:11px}
.story p{font-size:5.8px;color:var(--grey);line-height:10px;margin-top:5px;white-space:nowrap}

.site-footer{left:0;top:1044px;width:671px;height:156px;background:var(--footer);border-top:2px solid #888;color:var(--white)}
.footer-col h4{font-size:8.5px;font-weight:400;letter-spacing:.2px}
.contact-lines{font-size:6.8px;line-height:11px;margin-top:10px}
.contact-row{display:flex;align-items:center;gap:9px;margin-top:6px;font-size:7px}
.contact-row.phone{font-size:9.5px;letter-spacing:.5px}
.links-list{list-style:none;font-size:5.8px;line-height:11.5px;margin-top:8px}
.links-list li::before{content:"» ";}
.newsletter p{font-size:6px;line-height:11px;margin-top:9px;width:150px}
.signup{display:flex;margin-top:9px}
.signup .field{width:98px;height:22px;background:var(--white);color:#888;font-size:5.5px;padding:8px 6px}
.signup .btn{width:48px;height:22px;background:var(--green);font-size:8.5px;display:flex;align-items:center;justify-content:center}
.social{display:flex;gap:10px;margin-top:10px}
.social span{width:20px;height:20px;background:#e8e8e8;border-radius:3px}
.footer-rule{left:28px;top:1166px;width:615px;height:1px;background:var(--footer-line)}
.copyright{left:0;top:1174px;width:671px;text-align:center;font-size:7.5px;color:var(--white)}
</style>
</head>
<body>
<div class="abs top-line"></div>

<header class="abs site-header">
  <div class="abs brand"><span class="brand-mark"></span><span class="brand-name">VARNOLIX</span></div>
  <div class="abs lang">ENGLISH
    <svg width="5" height="4" viewBox="0 0 5 4"><path d="M.5 .8 2.5 2.8 4.5 .8" stroke="#fff" fill="none" stroke-width=".9"/></svg>
  </div>
  <nav class="abs main-nav">
    <span>NATURAL INTELLIGENCE</span><span>PRODUCTS</span><span>SERVICES</span><span>PARTNERS</span><span>CONTACT US</span><span>ABOUT</span>
  </nav>
</header>

<section class="abs hero" role="img" aria-label="Humanoid robot touching a holographic interface"></section>
<div class="abs hero-title">
  <div class="line1">QUILLET, BY VARNOLIX. THE NEW STANDARD</div>
  <div class="line2">IN CONTACT CENTER CUSTOMER EXPERIENCE</div>
</div>
<div class="abs slider-arrows">
  <span><svg width="6" height="8" viewBox="0 0 6 8"><path d="M4.5 1 1.5 4 4.5 7" stroke="#fff" fill="none" stroke-width="1.4"/></svg></span>
  <span><svg width="6" height="8" viewBox="0 0 6 8"><path d="M1.5 1 4.5 4 1.5 7" stroke="#fff" fill="none" stroke-width="1.4"/></svg></span>
</div>

<a class="abs cta cta-demo">
  <svg width="12" height="9" viewBox="0 0 12 9"><rect x="0" y="1" width="8" height="7" rx="1" fill="#fff"/><path d="M8 4.5 12 1.5V7.5Z" fill="#fff"/></svg>
  REQUEST A DEMO
</a>
<a class="abs cta cta-contact">
  <svg width="9" height="10" viewBox="0 0 9 10"><circle cx="4.5" cy="2.7" r="2.4" fill="#fff"/><path d="M0 10C0 6.5 2 5.4 4.5 5.4S9 6.5 9 10Z" fill="#fff"/></svg>
  CONTACT US
</a>

<h2 class="abs section-title news-title">RECENT <em>NEWS</em></h2>

<article class="abs news-card" style="left:50px;top:458px">
  <div class="photo" role="img" aria-label="Businessman pressing a virtual touchscreen" style="background:linear-gradient(150deg,#8fb3c4,#3d5866)"></div>
  <div class="caption">Neque porro quisquam est qui<br>ipsum quia dolor sit amet,<svg width="7" height="11" viewBox="0 0 7 11"><path d="M1 1 5.5 5.5 1 10" stroke="#fff" fill="none" stroke-width="1.8"/></svg></div>
</article>
<article class="abs news-card" style="left:245px;top:458px">
  <div class="photo" role="img" aria-label="Symmetrical robotic machinery in blue light" style="background:linear-gradient(160deg,#9ec6d2,#2f4d5c)"></div>
  <div class="caption">Neque porro quisquam est qui<br>ipsum quia dolor sit amet,<svg width="7" height="11" viewBox="0 0 7 11"><path d="M1 1 5.5 5.5 1 10" stroke="#fff" fill="none" stroke-width="1.8"/></svg></div>
</article>
<article class="abs news-card" style="left:439px;top:458px">
  <div class="photo" role="img" aria-label="Chrome robot beside a woman in a studio" style="background:linear-gradient(150deg,#b8bcc2,#5a5e66)"></div>
  <div class="caption">Neque porro quisquam est qui<br>ipsum quia dolor sit amet,<svg width="7" height="11" viewBox="0 0 7 11"><path d="M1 1 5.5 5.5 1 10" stroke="#fff" fill="none" stroke-width="1.8"/></svg></div>
</article>
<article class="abs news-card" style="left:50px;top:621px">
  <div class="photo" role="img" aria-label="Black robot head against a dusk sky" style="background:linear-gradient(170deg,#6d7e96,#3a3434)"></div>
  <div class="caption">Neque porro quisquam est qui<br>ipsum quia dolor sit amet,<svg width="7" height="11" viewBox="0 0 7 11"><path d="M1 1 5.5 5.5 1 10" stroke="#fff" fill="none" stroke-width="1.8"/></svg></div>
</article>
<article class="abs news-card" style="left:245px;top:621px">
  <div class="photo" role="img" aria-label="White robots walking through a city street" style="background:linear-gradient(170deg,#a59f95,#4b4a4a)"></div>
  <div class="caption">Neque porro quisquam est qui<br>ipsum quia dolor sit amet,<svg width="7" height="11" viewBox="0 0 7 11"><path d="M1 1 5.5 5.5 1 10" stroke="#fff" fill="none" stroke-width="1.8"/></svg></div>
</article>
<article class="abs news-card" style="left:439px;top:621px">
  <div class="photo" role="img" aria-label="Robot hand shaking a human hand among skyscrapers" style="background:linear-gradient(160deg,#8a9aa8,#454d57)"></div>
  <div class="caption">Neque porro quisquam est qui<br>ipsum quia dolor sit amet,<svg width="7" height="11" viewBox="0 0 7 11"><path d="M1 1 5.5 5.5 1 10" stroke="#fff" fill="none" stroke-width="1.8"/></svg></div>
</article>

<section class="abs stories"></section>
<h2 class="abs section-title stories-title">SUCCESS STORIES <em>FROM OUR PARTNERS</em></h2>

<div class="abs story" style="left:56px;top:883px">
  <div class="avatar" role="img" aria-label="Portrait of a partner"></div>
  <h3>Neque porro quisquam</h3>
  <p>Lorem Ipsum has been the industry's standard dummy<br>text ever since the 1500s, when an unknown printer<br>took a galley of type and scrambled it to make<br>a type specimen book</p>
</div>
<div class="abs story" style="left:251px;top:883px">
  <div class="avatar" role="img" aria-label="Portrait of a partner"></div>
  <h3>Neque porro quisquam</h3>
  <p>Lorem Ipsum has been the industry's standard dummy<br>text ever since the 1500s, when an unknown printer<br>took a galley of type and scrambled it to make<br>a type specimen book</p>
</div>
<div class="abs story" style="left:445px;top:883px">
  <div class="avatar" role="img" aria-label="Portrait of a partner"></div>
  <h3>Neque porro quisquam</h3>
  <p>Lorem Ipsum has been the industry's standard dummy<br>text ever since the 1500s, when an unknown printer<br>took a galley of type and scrambled it to make<br>a type specimen book</p>
</div>

<footer class="abs site-footer">
  <div class="abs footer-col" style="left:51px;top:20px">
    <h4>CONTACT US</h4>
    <div class="contact-lines">42 Harlow Lane 3rd Floor<br>Brookfield, BK 20415</div>
    <div class="contact-row phone">
      <svg width="10" height="10" viewBox="0 0 10 10"><path d="M2 .8 3.6 2.6 2.8 3.8Q4 6 6.2 7.2L7.4 6.4 9.2 8 8.2 9.3Q4.5 9 1.9 6.1T.8 1.8Z" stroke="#fff" fill="none" stroke-width=".8"/></svg>
      0400 555 018
    </div>
    <div class="contact-row">
      <svg width="10" height="8" viewBox="0 0 10 8"><rect x=".5" y=".5" width="9" height="7" stroke="#fff" fill="none" stroke-width=".8"/><path d="M.5 .5 5 4.5 9.5 .5" stroke="#fff" fill="none" stroke-width=".8"/></svg>
      hello@varnolix-mail.net
    </div>
  </div>
  <div class="abs footer-col" style="left:216px;top:20px">
    <h4>LINKS</h4>
    <ul class="links-list">
      <li>Natural Intelligence</li><li>Products</li><li>Sitemap</li><li>Terms of Use</li><li>Privacy Policy</li>
    </ul>
  </div>
  <div class="abs footer-col newsletter" style="left:355px;top:20px">
    <h4>NEWSLETTER</h4>
    <p>Excepteur sint occaecat cupidatat non proident, sunt in culpa qui officia deserunt mollit anim</p>
    <div class="signup"><span class="field">Enter your email address</span><span class="btn">Sign Up</span></div>
  </div>
  <div class="abs footer-col" style="left:541px;top:20px">
    <h4>SOCIAL MEDIA</h4>
    <div class="social"><span></span><span></span><span></span></div>
  </div>
</footer>
<div class="abs footer-rule"></div>
<div class="abs copyright">2016 &nbsp;All Rights Reserved.</div>
</body>
</html>
```